Nimbus Crest Plan- Brindlow Insurance providing specialist Cyber and Liability Insurance

for Managed Technology Service Providers and their customer, we will use a letterhead that white labels insurer documents, which can be used in our physical letters as well as to be used within Email signatures.

Target Market(s)

Managed Technology Services Providers

Industry/Entity Type

Cyber Insurance

Requirements
Must have
• website, email address, contact phone numbers

```html
<!DOCTYPE html>
<html lang="en">
<head>
<meta charset="utf-8">
<title>Nimbus Crest Plan – Letterhead</title>
<link rel="stylesheet" href="https://fonts.googleapis.com/css2?family=Poppins:wght@400;500;600&display=swap">
<style>
  :root {
    --paper: #f3f3f3;
    --ink: #3a3a3a;
    --header-band: #454545;
    --footer-band: #111111;
    --accent: #33a548;
    --white: #ffffff;
    --watermark: #e2e2e2;
    --divider: #6a6a6a;
  }
  * { box-sizing: border-box; margin: 0; padding: 0; }
  html, body { width: 898px; height: 1200px; overflow: hidden; background: var(--paper); }
  body { font-family: "Poppins", sans-serif; color: var(--ink); }

  .letterhead { position: relative; width: 898px; height: 1200px; background: var(--paper); overflow: hidden; }

  .band-shapes { position: absolute; inset: 0; }

  .brand {
    position: absolute;
    display: flex;
    align-items: center;
    gap: 8px;
    font-weight: 600;
    letter-spacing: 0.02em;
    white-space: nowrap;
  }
  .brand__mark { width: 12px; height: 12px; background: var(--accent); }
  .brand--header { left: 28px; top: 29px; font-size: 24px; color: var(--ink); }
  .brand--footer { right: 36px; top: 1150px; font-size: 18px; color: var(--white); }

  .contact {
    position: absolute;
    top: 14px;
    font-size: 14.5px;
    line-height: 20px;
    color: var(--white);
    font-weight: 400;
  }
  .contact--phones { left: 410px; }
  .contact--online { left: 566px; }
  .contact__row { display: flex; align-items: center; gap: 7px; height: 22px; }
  .contact__icon { width: 11px; height: 11px; flex: none; }

  .contact-divider {
    position: absolute;
    left: 545px; top: 18px;
    width: 1px; height: 40px;
    background: var(--divider);
  }

  .watermark {
    position: absolute;
    left: 812px; top: 330px;
    transform-origin: left top;
    transform: translate(60px, 0) rotate(90deg);
    font-size: 54px;
    font-weight: 500;
    color: var(--watermark);
    letter-spacing: 0.06em;
    white-space: nowrap;
  }

  .tagline {
    position: absolute;
    left: 30px; top: 1148px;
    font-size: 12.5px;
    color: var(--white);
    white-space: nowrap;
  }
</style>
</head>
<body>
  <main class="letterhead">
    <svg class="band-shapes" width="898" height="1200" viewBox="0 0 898 1200" aria-hidden="true">
      <polygon points="327,0 898,0 898,84 390,82" fill="var(--header-band)"/>
      <polygon points="0,1144 584,1146 562,1170 0,1171" fill="var(--accent)"/>
      <polygon points="0,1177 898,1177 898,1200 0,1200" fill="var(--footer-band)"/>
      <polygon points="620,1136 898,1137 898,1200 560,1200 556,1177 570,1175" fill="var(--footer-band)"/>
    </svg>

    <header>
      <div class="brand brand--header"><span class="brand__mark"></span>Nimbus Crest Plan</div>

      <div class="contact contact--phones">
        <div class="contact__row">
          <svg class="contact__icon" viewBox="0 0 24 24"><path fill="var(--accent)" d="M6.6 10.8a15 15 0 0 0 6.6 6.6l2.2-2.2a1 1 0 0 1 1-.25 11.4 11.4 0 0 0 3.6.57 1 1 0 0 1 1 1V20a1 1 0 0 1-1 1A17 17 0 0 1 3 4a1 1 0 0 1 1-1h3.5a1 1 0 0 1 1 1c0 1.25.2 2.45.57 3.6a1 1 0 0 1-.25 1z"/></svg>
          <span>555-014-2290</span>
        </div>
        <div class="contact__row">
          <svg class="contact__icon" viewBox="0 0 24 24"><path fill="var(--accent)" d="M6.6 10.8a15 15 0 0 0 6.6 6.6l2.2-2.2a1 1 0 0 1 1-.25 11.4 11.4 0 0 0 3.6.57 1 1 0 0 1 1 1V20a1 1 0 0 1-1 1A17 17 0 0 1 3 4a1 1 0 0 1 1-1h3.5a1 1 0 0 1 1 1c0 1.25.2 2.45.57 3.6a1 1 0 0 1-.25 1z"/></svg>
          <span>555-014-2290</span>
        </div>
      </div>

      <div class="contact-divider"></div>

      <div class="contact contact--online">
        <div class="contact__row">
          <svg class="contact__icon" viewBox="0 0 24 24"><circle cx="12" cy="12" r="10" fill="none" stroke="var(--accent)" stroke-width="2.4"/><path d="M2 12h20M12 2c3 3 3 17 0 20M12 2c-3 3-3 17 0 20" fill="none" stroke="var(--accent)" stroke-width="2"/></svg>
          <span>mara@nimbuscrestplan.com</span>
        </div>
        <div class="contact__row">
          <svg class="contact__icon" viewBox="0 0 24 24"><rect x="1" y="4" width="22" height="16" fill="var(--accent)"/><path d="M1 4l11 9 11-9" fill="none" stroke="var(--header-band)" stroke-width="1.8"/></svg>
          <span>www.nimbuscrestplan.com</span>
        </div>
      </div>
    </header>

    <div class="watermark" aria-hidden="true">Nimbus Crest Plan</div>

    <footer>
      <p class="tagline">Brindlow Insurance providing specialist Cyber and Liability Insurance</p>
      <div class="brand brand--footer">Nimbus Crest Plan</div>
    </footer>
  </main>
</body>
</html>
```